Tinder Hearth EPP Mailer

This card will be mailed to local communities to make people aware of the ALL the Products - particularly local food - offered at Tinder Hearth of Margaretville. On the attached copy, the content in BOLD should be emphasized. Not all of the photos need to be utilized, but wanted to provide an assortment that shows off food and merchandise. Please note - this card is 8 in. x 6.5 inches and MUST be laid out to conform the the Each Porch Post format attached - with mailing and postage spaces left in the areas indicated on one side.

```html
<!DOCTYPE html>
<html lang="en">
<head>
<meta charset="utf-8">
<title>Tinder Hearth EPP Mailer</title>
<link rel="stylesheet" href="https://fonts.googleapis.com/css2?family=Signika:wght@300;400;600;700&display=swap">
<style>
  :root {
    --backdrop: #7a7a7a;
    --card: #ffffff;
    --green: #55a136;
    --green-dark: #4a9230;
    --cream: #fdf9d3;
    --slate: #77777a;
    --ink: #3a3a3a;
    --white: #ffffff;
  }
  * { box-sizing: border-box; margin: 0; padding: 0; }
  html, body { width: 1200px; height: 904px; overflow: hidden; }
  body {
    background: var(--backdrop);
    font-family: "Signika", "Helvetica Neue", Arial, sans-serif;
    position: relative;
  }
  .mailer { position: absolute; width: 490px; height: 399px; background: var(--card); }
  .mailer--front { left: 186px; top: 39px; }
  .mailer--back { left: 524px; top: 465px; }
  .block { position: absolute; }

  .brand {
    background: var(--cream);
    color: var(--green-dark);
    font-weight: 400;
    display: flex; flex-direction: column; justify-content: center;
    padding-left: 10px;
    line-height: 1.05;
    border-bottom: 5px solid var(--green);
  }
  .brand--front { left: 15px; top: 15px; width: 175px; height: 58px; font-size: 16px; }
  .brand--back { left: 278px; top: 15px; width: 123px; height: 40px; font-size: 11.5px; padding-left: 7px; border-bottom-width: 4px; }

  .photo { position: absolute; }
  .photo--pantry { left: 194px; top: 15px; width: 281px; height: 196px; background: linear-gradient(160deg, #b88a55 0%, #6b4a2e 45%, #c45a2a 75%, #d8c08a 100%); }
  .photo--tins { left: 195px; top: 216px; width: 137px; height: 167px; background: linear-gradient(180deg, #d6658c 0%, #5c5f66 50%, #d9462e 100%); }
  .photo--produce { left: 336px; top: 216px; width: 139px; height: 167px; background: linear-gradient(180deg, #6e5c48 0%, #4f8fa2 45%, #c8763a 80%, #b4893f 100%); }
  .photo--bakery { left: 15px; top: 15px; width: 246px; height: 123px; background: linear-gradient(180deg, #b9a88f 0%, #8c7a63 45%, #c69a5a 80%, #7e6a52 100%); }
  .photo--flour { left: 15px; top: 142px; width: 121px; height: 92px; background: linear-gradient(180deg, #a8865a 0%, #7b6446 60%, #c9a36a 100%); }
  .photo--linens { left: 140px; top: 142px; width: 121px; height: 92px; background: linear-gradient(160deg, #9fce6e 0%, #7fb75a 40%, #d8cbb0 70%, #3c8fb2 100%); }

  .features { left: 15px; top: 78px; width: 175px; height: 213px; background: var(--green); color: var(--white); padding: 10px 9px; }
  .features__title { font-weight: 700; font-size: 16.4px; line-height: 1.16; text-transform: uppercase; margin-bottom: 4px; }
  .features__list { list-style: none; font-size: 9.6px; font-weight: 400; }
  .features__list li { display: flex; align-items: center; gap: 3px; height: 15px; }
  .features__list li.features__row { justify-content: space-between; gap: 0; }
  .features__row span { display: flex; align-items: center; gap: 3px; }
  .tick { width: 7px; height: 7px; flex: none; }
  .features__rule { border: 0; border-top: 1px solid rgba(255,255,255,.45); margin: 6px 0 7px; }
  .features__promise { font-weight: 700; font-size: 12.6px; line-height: 1.28; text-transform: uppercase; }

  .contact { background: var(--slate); color: var(--white); padding: 6px 9px; }
  .contact--front { left: 15px; top: 295px; width: 175px; height: 88px; }
  .contact--back { left: 15px; top: 327px; width: 246px; height: 57px; padding-top: 5px; }
  .contact__heading { font-weight: 600; font-size: 10.6px; margin-bottom: 2px; }
  .contact__line { display: flex; align-items: center; gap: 4px; font-size: 9.6px; font-weight: 300; height: 15px; }
  .contact--back .contact__line { font-size: 9.4px; height: 14px; }
  .contact__line span { display: flex; align-items: center; gap: 4px; margin-right: 6px; }
  .icon { width: 11px; height: 11px; flex: none; }
  .social { position: absolute; right: 7px; bottom: 7px; display: flex; gap: 3px; }
  .social i { display: block; width: 11px; height: 11px; border-radius: 50%; background: var(--white); }

  .story { left: 15px; top: 238px; width: 246px; height: 86px; background: var(--green); color: var(--white); padding: 7px 9px; font-size: 8.5px; line-height: 1.32; font-weight: 400; }
  .story strong { font-weight: 600; }
  .story__call { font-weight: 700; font-size: 9.2px; margin-top: 3px; }

  .return-address { left: 278px; top: 61px; font-size: 8.6px; color: var(--ink); font-weight: 400; }
  .indicia { left: 415px; top: 16px; width: 58px; height: 58px; border: 1px solid #a9a9a9; font-size: 5.8px; font-weight: 600; color: #222; text-align: center; display: flex; flex-direction: column; justify-content: center; line-height: 1.4; }
  .recipient { left: 278px; top: 240px; width: 151px; height: 48px; border: 1px solid #a9a9a9; font-size: 6px; font-weight: 600; color: #222; padding: 6px 7px; }
  .recipient__sort { text-align: right; letter-spacing: .2px; margin-bottom: 14px; }
  .recipient__name { line-height: 1.35; }
</style>
</head>
<body>
<svg width="0" height="0" style="position:absolute" aria-hidden="true">
  <defs>
    <symbol id="i-tick" viewBox="0 0 10 10"><circle cx="5" cy="5" r="5" fill="#fff"/><path d="M2.6 5.2 4.3 6.8 7.4 3.6" fill="none" stroke="#55a136" stroke-width="1.4" stroke-linecap="round" stroke-linejoin="round"/></symbol>
    <symbol id="i-pin" viewBox="0 0 12 12"><circle cx="6" cy="6" r="6" fill="#fff"/><path d="M6 2.6a2.2 2.2 0 0 0-2.2 2.2C3.8 6.5 6 9.3 6 9.3s2.2-2.8 2.2-4.5A2.2 2.2 0 0 0 6 2.6z" fill="#77777a"/><circle cx="6" cy="4.8" r=".8" fill="#fff"/></symbol>
    <symbol id="i-phone" viewBox="0 0 12 12"><circle cx="6" cy="6" r="6" fill="#fff"/><path d="M4.1 3c.4 0 .6.9.8 1.3.1.3-.5.6-.5.8.3.8 1 1.5 1.8 1.8.2 0 .5-.6.8-.5.4.2 1.3.4 1.3.8 0 .6-.6 1.3-1.3 1.2C5 8.2 3.8 7 3.6 4.3 3.5 3.6 3.6 3 4.1 3z" fill="#77777a"/></symbol>
    <symbol id="i-mail" viewBox="0 0 12 12"><circle cx="6" cy="6" r="6" fill="#fff"/><rect x="3" y="3.9" width="6" height="4.2" rx=".4" fill="#77777a"/><path d="M3.2 4.1 6 6.3l2.8-2.2" fill="none" stroke="#fff" stroke-width=".6"/></symbol>
    <symbol id="i-web" viewBox="0 0 12 12"><circle cx="6" cy="6" r="6" fill="#fff"/><g fill="none" stroke="#77777a" stroke-width=".6"><circle cx="6" cy="6" r="3.3"/><ellipse cx="6" cy="6" rx="1.4" ry="3.3"/><path d="M2.7 6h6.6M3.2 4.4h5.6M3.2 7.6h5.6"/></g></symbol>
  </defs>
</svg>

<section class="mailer mailer--front" aria-label="Mailer front">
  <div class="block brand brand--front"><span>Tinder Hearth</span><span>of Margaretville</span></div>

  <div class="block features">
    <h1 class="features__title">Tinder Hearth of Margaretville proudly features:</h1>
    <ul class="features__list">
      <li><svg class="tick"><use href="#i-tick"/></svg>Local Produce, Meat &amp; Cheese</li>
      <li><svg class="tick"><use href="#i-tick"/></svg>Local Breads &amp; Sweets</li>
      <li><svg class="tick"><use href="#i-tick"/></svg>International Foods</li>
      <li class="features__row">
        <span><svg class="tick"><use href="#i-tick"/></svg>Kitchen</span>
        <span><svg class="tick"><use href="#i-tick"/></svg>Home</span>
        <span><svg class="tick"><use href="#i-tick"/></svg>Gift Items</span>
      </li>
    </ul>
    <hr class="features__rule">
    <p class="features__promise">Open 7 days!<br>Family-run<br>Locally focused<br>Kind service</p>
  </div>

  <div class="block contact contact--front">
    <p class="contact__heading">Corner of Elm &amp; Mill Streets</p>
    <p class="contact__line"><svg class="icon"><use href="#i-pin"/></svg>212 Elm Street, Margaretville</p>
    <p class="contact__line"><svg class="icon"><use href="#i-phone"/></svg>845 555-0142</p>
    <p class="contact__line"><svg class="icon"><use href="#i-mail"/></svg>hello@tinderhearth.net</p>
    <p class="contact__line"><svg class="icon"><use href="#i-web"/></svg>www.tinderhearth.net</p>
    <div class="social" aria-hidden="true"><i></i><i></i></div>
  </div>

  <div class="photo photo--pantry" role="img" aria-label="Photo of store shelves stocked with sauces, jars of sauerkraut and noodle packets"></div>
  <div class="photo photo--tins" role="img" aria-label="Photo of round gift tins with cassette-tape designs"></div>
  <div class="photo photo--produce" role="img" aria-label="Photo of the produce stand with baskets of fresh fruit and vegetables"></div>
</section>

<section class="mailer mailer--back" aria-label="Mailer back">
  <div class="photo photo--bakery" role="img" aria-label="Photo of a bakery case filled with cookies, scones and pastries"></div>
  <div class="photo photo--flour" role="img" aria-label="Photo of bags of local flour and loaves of bread"></div>
  <div class="photo photo--linens" role="img" aria-label="Photo of home goods shelves with pillows and kitchen towels"></div>

  <div class="block story">
    <p>Discover our many <strong>RegionalFood Items.</strong><br>
    Choosing locally grown/produced, healthyfoodbenefits you, your neighbors &amp; our planet. We like that.<br>
    Please stop in &amp; see the changes we have in store...with more to come!</p>
    <p class="story__call">Make A Day of It Downtown!</p>
  </div>

  <div class="block contact contact--back">
    <p class="contact__heading">Corner of Elm &amp; Mill Streets</p>
    <p class="contact__line"><span><svg class="icon"><use href="#i-phone"/></svg>845 555-0142</span><span><svg class="icon"><use href="#i-web"/></svg>www.tinderhearth.net</span></p>
    <p class="contact__line"><svg class="icon"><use href="#i-mail"/></svg>hello@tinderhearth.net</p>
    <div class="social" aria-hidden="true"><i></i><i></i></div>
  </div>

  <div class="block brand brand--back"><span>Tinder Hearth</span><span>of Margaretville</span></div>
  <p class="block return-address">212 Elm Street, Margaretville</p>

  <div class="block indicia"><span>PRSRT STD</span><span>ECRWSS</span><span>U.S. POSTAGE</span><span>PAID</span><span>EPPM-Retail</span></div>

  <div class="block recipient">
    <p class="recipient__sort">****************ECRWSS****</p>
    <p class="recipient__name">Local<br>Postal Customer</p>
  </div>
</section>
</body>
</html>
```